Liam Kovac Fitness Business Card

I Need a really cool and creative yet modern and cutting edge. I run a personal training company, I have a logo already which ill submit images of. Id like the base colors to be black and white with a little red as a highlight color. Charcoal grey is fine also. My clientele is mostly comprised of young professionals who are in touch with modern culture art and are interested in "cool" so if there was one thing i want this business card to be it sexy and cool.

Target Market(s)

young professionals who are image conscious, care about their health, looking and feeling good. They know what is cool and expect the best.

Industry/Entity Type

Training

Requirements
Must have
• - must be a 2 sided card
- must include the following:

Liam Kovac CPT
646 392 7105
Liam@LiamKovacFitness.example
www.LiamKovacFitness.example
Nice to have
• id like to see some unconventional shape ideas as well as conventional ones

```html
<!DOCTYPE html>
<html lang="en">
<head>
<meta charset="utf-8">
<title>Liam Kovac Fitness – Business Card</title>
<link rel="stylesheet" href="https://fonts.googleapis.com/css2?family=Questrial&display=swap">
<style>
  :root {
    --paper: #ffffff;
    --ink: #111212;
    --charcoal: #1a1b1b;
    --accent: #e3141b;
    --edge: #dcdcdc;
    --stage: #ffffff;
  }
  * { box-sizing: border-box; margin: 0; padding: 0; }
  html, body {
    width: 1200px;
    height: 720px;
    overflow: hidden;
    background: var(--stage);
  }
  .canvas {
    position: relative;
    width: 1200px;
    height: 720px;
    font-family: "Questrial", "Century Gothic", sans-serif;
    color: var(--ink);
  }
  .card {
    position: absolute;
    width: 683px;
    height: 388px;
    background: var(--paper);
    border: 1px solid var(--edge);
    overflow: hidden;
  }
  .card--front { left: 22px; top: 25px; z-index: 2; }
  .card--back  { left: 455px; top: 263px; z-index: 1; }

  .brand {
    position: absolute;
    left: 72px;
    top: 118px;
    display: flex;
    align-items: flex-start;
    gap: 14px;
  }
  .brand__name {
    font-size: 46px;
    line-height: 1.08;
    color: var(--ink);
    letter-spacing: 0.5px;
  }
  .brand__mark {
    width: 16px;
    height: 16px;
    margin-top: 8px;
    background: var(--accent);
  }

  .athlete {
    position: absolute;
    left: 383px;
    top: 50px;
    width: 300px;
    height: 338px;
    background: linear-gradient(180deg, var(--charcoal), #0b0b0b);
    border-radius: 40px 0 0 18px;
  }

  .contact {
    position: absolute;
    left: 0;
    width: 683px;
    top: 146px;
    padding-left: 0;
    text-align: center;
    transform: translateX(-2px);
  }
  .contact__list {
    list-style: none;
    font-size: 16px;
    line-height: 20px;
    color: var(--ink);
  }
  .contact__name { letter-spacing: 0.2px; }
</style>
</head>
<body>
  <main class="canvas">
    <section class="card card--front" aria-label="Card front">
      <div class="brand">
        <span class="brand__name">Liam Kovac<br>Fitness</span>
        <span class="brand__mark" aria-hidden="true"></span>
      </div>
      <div class="athlete" role="img" aria-label="Black silhouette of a person holding a forearm plank, cropped at the card's right edge"></div>
    </section>

    <section class="card card--back" aria-label="Card back">
      <address class="contact">
        <ul class="contact__list">
          <li class="contact__name">Liam Kovac CPT</li>
          <li class="contact__phone">646 392 7105</li>
          <li class="contact__email">Liam@LiamKovacFitness.example</li>
          <li class="contact__web">www.LiamKovacFitness.example</li>
        </ul>
      </address>
    </section>
  </main>
</body>
</html>
```